Building Maintenance Flyer specialising in hot and silent pressure cleaning

Hi. I love this flyer. I would like something similar but with hot water pressure washing and building maintenance

Ferro Lane & Services provides high pressure steam cleaning and water blasting services throughout Brisbane and surrounding areas, covering the Industrial, Commercial, Strata and Residential property owners sectors.

FLS combining the cleaning power of heat with state-of-the-art silent equipment, accredited technicians and a steadfast commitment to the environment. We offer the best Prompt, Professional Service.

Fully Accredited & Certified Technicians
100% Satisfaction Guaranteed
We are a family owned and operated business and love what we do. No job is too big or too small and we take pride in our work.
All of our services are undertaken using industry leading equipment and, providing safe and superior results.

Our business is covered by 20 million full public liability insurance and we operate within strict health & safety guidelines, providing all our clients with complete peace of mind. Project plans and risk assessments can also be provided upon request.

BODY CORPORATES

BUILDING FAÇADE CLEANING

CAR PARKS – underground, single and multi level

DRIVE THRU

FOOD PRODUCTION FACILITIES CLEANING SANITISING

SHOPPING CENTRES

BIRD MANAGEMENT AND DECONTAMINATION

GENERAL MAINTENANCE

CONSTRUCTION CLEAN UPS

SPILL MANAGEMENT

CONCRETE CLEANING AND DEGRASING

CONCRETE SEALING

FACTORY CLEANING & CLEAN UP

ENVIRONMENTAL DECONTAMINATION OF HEAVY VEHICLES AND EQUIPMENT

SITE CLEANS AND RUBBISH REMOVAL

MANUFACTURING PLANTS

Target Market(s)

Facility Managers, Commercial and Industrial Property Owners, Property Managers, Schools, Restaurants,

Industry/Entity Type

Pressure Cleaning

Font styles to use
Sans Serif

Colors
0293ce
00a990
33a6d7
33b8a4

Requirements
Must have
• SILENT HOT WATER PRESSURE CLEANING
Runs up to 120 Degrees Celsius
SANITISING - Bin areas, outdoor areas, cafe's, restaurants, schools, drive thru's
Blue's and Greens to link in with our logo

```html
<!DOCTYPE html>
<html lang="en">
<head>
<meta charset="utf-8">
<title>Ferro Lane &amp; Services – Commercial &amp; Industrial Property Maintenance Flyer</title>
<link href="https://fonts.googleapis.com/css2?family=Montserrat:wght@400;500;600;700;800&display=swap" rel="stylesheet">
<style>
  :root {
    --blue: #0293ce;
    --blue-head: #1b8fd2;
    --blue-soft: #33a6d7;
    --blue-band: #bfe4f0;
    --teal: #33b8a4;
    --teal-deep: #00a990;
    --mint: #a6e6da;
    --ink: #333a40;
    --ink-dark: #22313b;
    --page: #e4e4e4;
    --white: #ffffff;
  }
  * { box-sizing: border-box; margin: 0; padding: 0; }
  html, body {
    width: 1200px; height: 2357px; overflow: hidden;
    background: var(--page);
    font-family: "Montserrat", Arial, sans-serif;
  }
  .flyer {
    position: absolute; left: 89px; top: 818px;
    width: 1021px; height: 720px; overflow: hidden;
    background: var(--white);
    box-shadow: 0 6px 18px rgba(0,0,0,.18);
  }
  .flyer-art { position: absolute; inset: 0; width: 1021px; height: 720px; }
  .layer { position: absolute; }

  .brand { left: 526px; top: 40px; display: flex; align-items: center; gap: 12px; }
  .brand-dot { width: 44px; height: 44px; border-radius: 50%; background: var(--blue); }
  .brand-name { font-weight: 800; font-size: 40px; color: var(--blue-head); letter-spacing: 1px; }

  .headline { left: 527px; top: 118px; color: var(--blue-head); }
  .headline .line-1 { font-weight: 800; font-size: 40px; line-height: 44px; letter-spacing: .5px; }
  .headline .line-2 { font-weight: 800; font-size: 24px; line-height: 30px; letter-spacing: .6px; }
  .headline .line-3 { font-weight: 800; font-size: 31px; line-height: 38px; color: var(--ink); letter-spacing: .6px; }
  .tagline { left: 527px; top: 234px; font-size: 18px; line-height: 19px; color: var(--ink); }

  .features { left: 541px; top: 296px; list-style: none; }
  .features li { display: flex; align-items: center; gap: 14px; height: 42px; font-size: 14px; line-height: 14px; color: var(--ink-dark); font-weight: 500; }
  .features svg { width: 26px; height: 26px; flex: none; }

  .worker-photo { left: 842px; top: 276px; width: 168px; height: 392px; border-radius: 80px 80px 10px 10px; }

  .pitch { left: 525px; top: 426px; font-size: 20px; line-height: 23px; color: var(--ink); font-weight: 500; }
  .section-title { left: 525px; top: 516px; font-size: 21px; font-weight: 700; color: var(--blue-head); border-bottom: 2px solid var(--blue-head); letter-spacing: .5px; }
  .checklist { left: 524px; top: 556px; list-style: none; display: grid; grid-template-columns: 151px 160px; row-gap: 4px; }
  .checklist li { display: flex; align-items: center; gap: 7px; font-size: 15px; line-height: 21px; color: var(--ink); }
  .checklist svg { width: 15px; height: 15px; flex: none; }

  .contact { left: 492px; top: 684px; display: flex; align-items: center; gap: 14px; font-size: 14px; color: var(--ink-dark); font-weight: 500; }
  .contact .item { display: flex; align-items: center; gap: 7px; }
  .contact svg { width: 17px; height: 17px; }
  .contact .sep { font-weight: 600; }

  .solutions-title { left: 38px; top: 444px; font-size: 29px; font-weight: 700; color: var(--white); }
  .solutions { left: 40px; top: 496px; list-style: none; display: grid; grid-template-columns: 186px 170px; row-gap: 15px; }
  .solutions li { display: flex; align-items: center; gap: 12px; height: 38px; font-size: 11.5px; line-height: 12px; color: var(--white); }
  .solutions svg { width: 30px; height: 30px; flex: none; }

  .badge { left: 366px; top: 447px; width: 106px; height: 106px; border-radius: 50%;
    background: var(--blue); border: 4px solid var(--white); box-shadow: 0 3px 8px rgba(0,0,0,.3);
    display: flex; flex-direction: column; align-items: center; justify-content: center; color: var(--white); text-align: center; }
  .badge-value { font-weight: 800; font-size: 27px; line-height: 28px; }
  .badge-text { font-weight: 700; font-size: 7.5px; line-height: 10px; }
  .badge-text strong { font-size: 9px; }
</style>
</head>
<body>
<main class="flyer">
  <svg class="flyer-art" viewBox="0 0 1021 720" xmlns="http://www.w3.org/2000/svg">
    <defs>
      <linearGradient id="photoTone" x1="0" y1="0" x2="0" y2="1">
        <stop offset="0" stop-color="#e6e4f6"/>
        <stop offset=".5" stop-color="#cfcdec"/>
        <stop offset=".62" stop-color="#b84a4f"/>
        <stop offset="1" stop-color="#d98a8c"/>
      </linearGradient>
      <linearGradient id="panelTone" x1="0" y1="0" x2="0" y2="1">
        <stop offset="0" stop-color="#ffffff"/>
        <stop offset=".35" stop-color="#f1f8fa"/>
        <stop offset="1" stop-color="#dff3f1"/>
      </linearGradient>
      <linearGradient id="workerTone" x1="0" y1="0" x2="0" y2="1">
        <stop offset="0" stop-color="#f2d34a"/>
        <stop offset=".15" stop-color="#2c3550"/>
        <stop offset=".85" stop-color="#2c3550"/>
        <stop offset="1" stop-color="#2f8a5a"/>
      </linearGradient>
    </defs>
    <rect role="img" aria-label="Photo: technician in protective suit pressure cleaning a food production floor" x="0" y="0" width="520" height="720" fill="url(#photoTone)"/>
    <circle cx="186" cy="650" r="318" fill="#f3c7cb" opacity=".6"/>
    <circle cx="200" cy="655" r="300" fill="var(--mint)"/>
    <circle cx="186" cy="650" r="282" fill="var(--teal)"/>
    <path d="M462,0 L510,0 C462,230 434,500 432,720 L398,720 C402,500 428,230 462,0 Z" fill="var(--blue)"/>
    <path d="M458,0 C425,200 410,350 404,430" fill="none" stroke="#151515" stroke-width="5"/>
    <path d="M508,0 L1021,0 L1021,720 L432,720 C434,500 462,230 508,0 Z" fill="url(#panelTone)"/>
    <path d="M460,285 L1021,285 L1021,407 L448,407 C451,365 455,325 460,285 Z" fill="var(--blue-band)"/>
    <rect x="432" y="670" width="589" height="50" fill="var(--white)"/>
  </svg>

  <div class="layer worker-photo" role="img" aria-label="Photo: worker in overalls and hard hat holding a hot water pressure washer" style="background: linear-gradient(180deg,#f2d34a 0,#2c3550 14%,#2c3550 86%,#2f8a5a 100%); opacity:.85;"></div>

  <div class="layer brand"><span class="brand-dot"></span><span class="brand-name">FLS</span></div>

  <h1 class="layer headline">
    <div class="line-1">ALL COMMERCIAL</div>
    <div class="line-2">&amp; INDUSTRIAL PROPERTY</div>
    <div class="line-3">MAINTENANCE</div>
  </h1>
  <p class="layer tagline">FLS – servicing Southeast’s Commercial<br>&amp; Industrial sector 24/7</p>

  <ul class="layer features">
    <li><svg viewBox="0 0 26 26"><circle cx="13" cy="13" r="11" fill="none" stroke="var(--blue)" stroke-width="2" stroke-dasharray="58 12"/><text x="13" y="16" font-size="8" font-weight="700" text-anchor="middle" fill="var(--blue)" font-family="Montserrat, sans-serif">24h</text></svg><span>We operate 24/7, 7 days<br>&nbsp;a week</span></li>
    <li><svg viewBox="0 0 26 26"><rect x="3" y="6" width="14" height="5" rx="1" fill="var(--blue)"/><rect x="8" y="2" width="4" height="5" fill="var(--blue)"/><path d="M17 9 h4 v4" fill="none" stroke="var(--blue)" stroke-width="2"/><path d="M13 14 C10 19 10 22 13 23 C16 22 16 19 13 14 Z" fill="var(--blue)"/></svg><span>Silent hot water pressure<br>cleaning 150degrees</span></li>
    <li><svg viewBox="0 0 26 26"><circle cx="13" cy="9" r="5" fill="none" stroke="var(--blue)" stroke-width="1.8"/><path d="M4 24 C4 17 22 17 22 24" fill="none" stroke="var(--blue)" stroke-width="1.8"/><rect x="9" y="10" width="8" height="3" rx="1" fill="var(--blue)"/></svg><span>COVID-19 Trained</span></li>
  </ul>

  <p class="layer pitch">Silent hot water<br>pressure cleaning Runs<br>up to 120 Degrees Celsius</p>
  <h2 class="layer section-title">SANITISING</h2>
  <ul class="layer checklist">
    <li><svg viewBox="0 0 16 16"><circle cx="8" cy="8" r="6.5" fill="none" stroke="var(--blue)" stroke-width="1.5"/><path d="M5 8 l2 2 l5 -5" fill="none" stroke="var(--blue)" stroke-width="1.6"/></svg>Bin areas</li>
    <li><svg viewBox="0 0 16 16"><circle cx="8" cy="8" r="6.5" fill="none" stroke="var(--blue)" stroke-width="1.5"/><path d="M5 8 l2 2 l5 -5" fill="none" stroke="var(--blue)" stroke-width="1.6"/></svg>Schools</li>
    <li><svg viewBox="0 0 16 16"><circle cx="8" cy="8" r="6.5" fill="none" stroke="var(--blue)" stroke-width="1.5"/><path d="M5 8 l2 2 l5 -5" fill="none" stroke="var(--blue)" stroke-width="1.6"/></svg>Outdoor areas</li>
    <li><svg viewBox="0 0 16 16"><circle cx="8" cy="8" r="6.5" fill="none" stroke="var(--blue)" stroke-width="1.5"/><path d="M5 8 l2 2 l5 -5" fill="none" stroke="var(--blue)" stroke-width="1.6"/></svg>Drive thru's</li>
    <li><svg viewBox="0 0 16 16"><circle cx="8" cy="8" r="6.5" fill="none" stroke="var(--blue)" stroke-width="1.5"/><path d="M5 8 l2 2 l5 -5" fill="none" stroke="var(--blue)" stroke-width="1.6"/></svg>cafe's</li>
    <li><svg viewBox="0 0 16 16"><circle cx="8" cy="8" r="6.5" fill="none" stroke="var(--blue)" stroke-width="1.5"/><path d="M5 8 l2 2 l5 -5" fill="none" stroke="var(--blue)" stroke-width="1.6"/></svg>Blue's &amp; Greens</li>
    <li><svg viewBox="0 0 16 16"><circle cx="8" cy="8" r="6.5" fill="none" stroke="var(--blue)" stroke-width="1.5"/><path d="M5 8 l2 2 l5 -5" fill="none" stroke="var(--blue)" stroke-width="1.6"/></svg>Restaurants</li>
  </ul>

  <div class="layer contact">
    <span class="item"><svg viewBox="0 0 18 18"><path d="M3 7 C3 3 15 3 15 7 L12 8 L11 6 H7 L6 8 Z M5 9 H13 L15 15 H3 Z" fill="var(--blue)"/></svg>555 014 2290</span>
    <span class="sep">|</span>
    <span class="item"><svg viewBox="0 0 18 18"><rect x="1.5" y="4" width="15" height="10" fill="none" stroke="var(--blue)" stroke-width="1.6"/><path d="M1.5 4 L9 10 L16.5 4" fill="none" stroke="var(--blue)" stroke-width="1.6"/></svg>info@ferrolane.com</span>
    <span class="sep">|</span>
    <span class="item"><svg viewBox="0 0 18 18"><circle cx="9" cy="9" r="7.5" fill="var(--blue)"/><path d="M1.5 9 H16.5 M9 1.5 C5 5 5 13 9 16.5 C13 13 13 5 9 1.5" fill="none" stroke="#fff" stroke-width="1"/></svg>ferrolane.com</span>
  </div>

  <h2 class="layer solutions-title">Solutions For</h2>
  <ul class="layer solutions">
    <li><svg viewBox="0 0 30 30"><circle cx="15" cy="15" r="8" fill="none" stroke="var(--ink-dark)" stroke-width="2"/><path d="M15 3 V7 M15 23 V27 M3 15 H7 M23 15 H27 M6.5 6.5 L9.3 9.3 M20.7 20.7 L23.5 23.5 M6.5 23.5 L9.3 20.7 M20.7 9.3 L23.5 6.5" stroke="var(--ink-dark)" stroke-width="2"/></svg><span>COVID-19 Infection<br>Control</span></li>
    <li><svg viewBox="0 0 30 30"><path d="M18 3 V20 M12 27 L15 20 H22 L25 27 Z" fill="none" stroke="var(--ink-dark)" stroke-width="2"/><rect x="3" y="20" width="6" height="7" fill="var(--ink-dark)"/></svg><span>Common Area<br>Cleaning</span></li>
    <li><svg viewBox="0 0 30 30"><rect x="6" y="8" width="18" height="12" fill="var(--ink-dark)"/><path d="M3 22 H27 V26 H3 Z" fill="var(--ink-dark)"/><rect x="10" y="11" width="3" height="3" fill="#fff"/><rect x="17" y="11" width="3" height="3" fill="#fff"/></svg><span>Building<br>Management</span></li>
    <li><svg viewBox="0 0 30 30"><path d="M8 9 H22 L20 27 H10 Z M6 6 H24 V9 H6 Z" fill="none" stroke="var(--ink-dark)" stroke-width="2"/></svg><span>Bird waste<br>removal</span></li>
    <li><svg viewBox="0 0 30 30"><rect x="5" y="12" width="10" height="15" fill="none" stroke="var(--ink-dark)" stroke-width="2"/><circle cx="21" cy="7" r="3.5" fill="var(--ink-dark)"/><path d="M21 11 V27" stroke="var(--ink-dark)" stroke-width="3"/></svg><span>Bin Cleaning<br>&amp; Sanitisation</span></li>
    <li><svg viewBox="0 0 30 30"><rect x="11" y="12" width="9" height="15" rx="2" fill="var(--ink-dark)"/><path d="M12 7 H20 V12 H13 Z" fill="var(--ink-dark)"/><path d="M4 5 L8 7 M4 9 H8 M5 13 L8 11" stroke="var(--ink-dark)" stroke-width="1.5"/></svg><span>Mould &amp; Mildew<br>removal</span></li>
    <li><svg viewBox="0 0 30 30"><circle cx="10" cy="7" r="3" fill="var(--ink-dark)"/><path d="M10 11 V20 L6 27 M10 20 L15 27 M10 14 L18 12 M20 6 V24 M16 24 H26" fill="none" stroke="var(--ink-dark)" stroke-width="2"/></svg><span>Garden<br>Maintenance</span></li>
    <li><svg viewBox="0 0 30 30"><circle cx="15" cy="17" r="7" fill="none" stroke="var(--ink-dark)" stroke-width="2"/><path d="M2 14 H8 V20 H2 M28 14 H22 V20 H28 M15 3 V10 M11 4 H19" fill="none" stroke="var(--ink-dark)" stroke-width="2"/></svg><span>Oil and Grease<br>elimination</span></li>
  </ul>

  <div class="layer badge">
    <div class="badge-value">100%</div>
    <div class="badge-text">ALL SATISFACTION<br><strong>GUARANTEED</strong></div>
  </div>
</main>
</body>
</html>
```